Newsletter Design Project

We need a newsletter design for our foundation based in the Philippines. We are a child care organization that works for the promotion and protection of children's rights. The newsletter design should be created in ACYMailing to be used on our Joomla website. The design should reflect the style and coulours of our website design. It should be compatible to view in web browsers and email applications. You can view our website at: www.brindlecovefoundation.org

If this process goes well, we would be interested to redesign our Carry the Lantern website (www.carrythelantern.net)
Updates

Reason: To give enough time for adjustment to a design a may like. I will have to share them with others whom I work with to get their feedback.

Reason: I'm interested in more designs and giving time for one designer to work with the code for my design template...

Target Market(s)

Youth/Adults/NGOs/Donors, etc

Industry/Entity Type

Foundation

Requirements
Must have
• must have menu
Donate button

```html
<!DOCTYPE html>
<html lang="en">
<head>
<meta charset="utf-8">
<title>Brindlecove Foundation Newsletter</title>
<link href="https://fonts.googleapis.com/css2?family=Arimo:ital,wght@0,400;0,700;1,700&display=swap" rel="stylesheet">
<style>
:root{
  --cream:#fcf8ec;
  --orange:#ff6600;
  --orange-dark:#e65400;
  --text:#4a4a4a;
  --heading:#555555;
  --frame:#d6d6d6;
  --footer:#ececec;
  --white:#ffffff;
}
*{box-sizing:border-box;margin:0;padding:0}
html,body{width:1200px;height:2250px;overflow:hidden;background:var(--cream);font-family:"Arimo",Helvetica,Arial,sans-serif;color:var(--text)}
.page{position:relative;width:1200px;height:2250px}
.topbar{position:absolute;top:41px;left:150px;width:900px;display:flex;justify-content:space-between;font-size:19px;line-height:22px}
.topbar .date{color:var(--orange)}
.topbar .menu span{margin:0 24px}
.sheet{position:absolute;top:75px;left:150px;width:900px;height:1841px;background:var(--white);border:1px solid var(--frame);border-top:13px solid var(--orange)}
.masthead{position:absolute;left:0;top:0;width:898px;height:147px;display:flex;align-items:center;justify-content:center;gap:20px;box-shadow:0 10px 12px -10px rgba(0,0,0,.12)}
.mark{width:68px;height:68px;background:var(--orange);border-radius:50%}
.brand .name{font-size:31px;letter-spacing:1px;color:#222;line-height:36px}
.brand .tag{font-size:18px;color:#222;margin-top:4px}
.abs{position:absolute}
.photo-frame{border:1px solid var(--frame);padding:6px;background:var(--white)}
.fill{display:block;width:100%;height:100%}
.hero{left:29px;top:200px;width:842px;height:222px}
h2{font-size:27px;line-height:31px;font-weight:700;color:var(--orange)}
.intro{left:29px;top:440px;width:842px}
.intro p{font-size:18px;line-height:30px;margin-top:5px}
.rule{height:2px;background:var(--orange)}
.donate-row{left:29px;top:620px;width:842px;height:62px}
.donate-row .rule{position:absolute;left:0;right:0;top:30px}
.donate{position:absolute;left:270px;width:300px;height:62px;display:flex;background:var(--orange);border:2px solid var(--orange-dark);border-radius:3px}
.donate span{flex:1;display:flex;align-items:center;justify-content:center;font-size:26px;font-weight:700;font-style:italic;color:#222}
.donate span+span{border-left:2px solid var(--orange-dark)}
.latest{left:29px;top:704px}
.article{left:29px;width:842px;height:155px}
.article .thumb{position:absolute;left:0;top:0;width:260px;height:155px}
.article .badge{position:absolute;left:7px;bottom:14px;width:140px;height:27px;background:var(--orange);color:var(--white);font-size:17px;line-height:19px;padding:4px 8px}
.article .body{position:absolute;left:293px;top:-6px;width:549px}
.article h3{font-size:17px;font-weight:700;color:var(--heading);line-height:26px}
.article p{font-size:17px;line-height:27px;margin-top:6px}
.article a{color:var(--orange);text-decoration:none}
.divider{left:29px;top:1315px;width:842px;height:2px;background:#8a8a8a}
.film{top:1343px;width:260px;height:372px}
.film .thumb{height:152px}
.film h4{font-size:22px;line-height:26px;font-weight:700;color:var(--heading);margin-top:21px}
.film p{font-size:17.5px;line-height:27px;margin-top:10px;width:260px}
.film .btn{position:absolute;top:324px;left:0;width:170px;height:48px;background:var(--orange);border:2px solid var(--orange-dark);border-radius:3px;color:var(--white);font-size:19px;display:flex;align-items:center;justify-content:center}
.foot{left:0;top:1769px;width:898px;height:58px;background:var(--footer);display:flex;align-items:center;justify-content:space-between;padding:0 29px}
.foot .note{font-size:15.5px;white-space:nowrap}
.foot .note u{text-decoration:underline}
.social{display:flex;gap:16px;font-size:14px;font-weight:700;color:var(--heading);white-space:nowrap}
.copyright{position:absolute;top:1943px;left:0;width:1200px;text-align:center;font-size:15px;color:#333}
</style>
</head>
<body>
<div class="page">
  <div class="topbar">
    <div class="date">05 December 2012</div>
    <div class="menu">Unsubscribe<span>|</span>Help<span>|</span>View Online</div>
  </div>

  <div class="sheet">
    <header class="masthead">
      <div class="mark"></div>
      <div class="brand">
        <div class="name">BRINDLECOVE FOUNDATION INC.</div>
        <div class="tag">a learning and resource center for children's rights</div>
      </div>
    </header>

    <div class="abs hero photo-frame">
      <svg class="fill" role="img" aria-label="Black and white photograph of a child looking up behind a chain-link fence" preserveAspectRatio="none" viewBox="0 0 10 10">
        <defs><linearGradient id="g1" x1="0" x2="1"><stop offset="0" stop-color="#1a1a1a"/><stop offset=".5" stop-color="#777"/><stop offset="1" stop-color="#222"/></linearGradient></defs>
        <rect width="10" height="10" fill="url(#g1)"/>
      </svg>
    </div>

    <section class="abs intro">
      <h2>Get Involved &amp; Support Us!</h2>
      <p>Child sexual abuse is a horrible crime that exists and thrives under a blanket of silence. In the Philippines, Brindlecove is setting up and training a national network of NGOs to address the issue of child sexual abuse and exploitation. The Carry the Lantern (CTL) Philippines network will count no less than 50 capacitated organizations spread around the archipelago within the coming 5 years.</p>
    </section>

    <div class="abs donate-row">
      <div class="rule"></div>
      <div class="donate"><span>Donate</span><span>QuickPay</span></div>
    </div>

    <h2 class="abs latest">Our Latest Articles</h2>

    <article class="abs article" style="top:760px">
      <div class="thumb photo-frame">
        <svg class="fill" role="img" aria-label="Film forum poster on dark background with green accents" preserveAspectRatio="none" viewBox="0 0 10 10"><rect width="10" height="10" fill="#2b2b2b"/><rect width="1.2" height="10" fill="#8dbb3c"/></svg>
      </div>
      <div class="badge">FEB 2012</div>
      <div class="body">
        <h3>HIHD 2012 Film Forum: Fighting Trafficking Through Film</h3>
        <p>Globally 1 million children are exploited by the commercial sex trade each year. Film reaches the soul and ceates lasting empathy. Brindlecove's third animated film, Paper Lanterns, was screeened last February 4, 2012 at the Harbor Initiative (HIHD). <a href="#">Read more...</a></p>
      </div>
    </article>

    <article class="abs article" style="top:945px">
      <div class="thumb photo-frame">
        <svg class="fill" role="img" aria-label="Photograph of police officers holding teaching dolls at a training session" preserveAspectRatio="none" viewBox="0 0 10 10"><defs><linearGradient id="g2" x1="0" x2="1"><stop offset="0" stop-color="#4f6a8a"/><stop offset="1" stop-color="#9a8a78"/></linearGradient></defs><rect width="10" height="10" fill="url(#g2)"/></svg>
      </div>
      <div class="badge">FEB 2012</div>
      <div class="body">
        <h3>A better way to interview children about sexaul abuse</h3>
        <p>The process of interviewing children--especially very young children in sexual abuse cases can be a trying experience for both the child and the interviewer. How can we get the information we need to protect the child, without causing more emotional trauma? <a href="#">Read more...</a></p>
      </div>
    </article>

    <article class="abs article" style="top:1132px">
      <div class="thumb photo-frame">
        <svg class="fill" role="img" aria-label="Photograph of schoolchildren sharing a meal" preserveAspectRatio="none" viewBox="0 0 10 10"><defs><linearGradient id="g3" x1="0" x2="1"><stop offset="0" stop-color="#6a4a3a"/><stop offset=".6" stop-color="#c77aa8"/><stop offset="1" stop-color="#8a6a5a"/></linearGradient></defs><rect width="10" height="10" fill="url(#g3)"/></svg>
      </div>
      <div class="badge">FEB 2012</div>
      <div class="body">
        <h3>When there is not enough to eat, school can quickly become an afterthought.</h3>
        <p>With active participation from the parents, Brindlecove's Community Assistance Program now prepares and serves a nutritious meal for the students everyday. School attendance has more than tripled and the students are more alert and ready to learn. <a href="#">Read more...</a></p>
      </div>
    </article>

    <div class="abs divider"></div>

    <div class="abs film" style="left:29px">
      <div class="thumb photo-frame"><svg class="fill" role="img" aria-label="Animated film artwork with red flowers" preserveAspectRatio="none" viewBox="0 0 10 10"><defs><linearGradient id="g4" x1="0" x2="1"><stop offset="0" stop-color="#c8202a"/><stop offset="1" stop-color="#3a6a2a"/></linearGradient></defs><rect width="10" height="10" fill="url(#g4)"/></svg></div>
      <h4>Paper Lanterns</h4>
      <p>Paper Lanterns tells the story of many young girls who are trafficked everyday as a result of poverty.</p>
      <div class="btn">Read More</div>
    </div>

    <div class="abs film" style="left:320px">
      <div class="thumb photo-frame"><svg class="fill" role="img" aria-label="Animated film artwork of street children on a grey wall" preserveAspectRatio="none" viewBox="0 0 10 10"><defs><linearGradient id="g5" x1="0" x2="1"><stop offset="0" stop-color="#8a8478"/><stop offset="1" stop-color="#c8b89a"/></linearGradient></defs><rect width="10" height="10" fill="url(#g5)"/></svg></div>
      <h4>A Brave Heart</h4>
      <p>A Brave Heart is a powerful depiction of the crime of pedophilia. Tale about young street kid named Miguel.</p>
      <div class="btn">Read More</div>
    </div>

    <div class="abs film" style="left:610px">
      <div class="thumb photo-frame"><svg class="fill" role="img" aria-label="Animated film artwork on purple background" preserveAspectRatio="none" viewBox="0 0 10 10"><defs><linearGradient id="g6" x1="0" x2="1"><stop offset="0" stop-color="#6a1a8a"/><stop offset="1" stop-color="#9a3aa8"/></linearGradient></defs><rect width="10" height="10" fill="url(#g6)"/></svg></div>
      <h4>Sister</h4>
      <p>Sister is a story about a young girl who left with the responsibility of taking care of her parents works overseas.</p>
      <div class="btn">Read More</div>
    </div>

    <footer class="abs foot">
      <div class="note">You received this email because you register in <u>brindlecovefoundation.org</u></div>
      <div class="social"><span>Facelink</span><span>Chirper</span><span>Vidstream</span><span>Photoreel</span></div>
    </footer>
  </div>

  <div class="copyright">2012 Brindlecove Foundation All Right Reserved.</div>
</div>
</body>
</html>
```